nutrition company business card

I would like to have a business card that has two sides, one being the green color from the Company name on the logo. I am open to ideas and looks that work with my logo. I like the idea of having a negative image of the tree on the green side.

For my information on the card I must have:
Linda Moorcombe
415-872-6041
lindamoorcombe@quellmail.net

This area will need to be updated once I complete my schooling.

Reason: I need to extend my deadline by one day as I have been sick the last week and not had time to review all the new designs. Thank you.

Industry/Entity Type

Nutrition

Requirements
Must have
• I would like to have a business card that has two sides, one being the green color from the Company name on the logo. I am open to ideas and looks that work with my logo. I like the idea of having a negative image of the tree on the green side.
• For my information on the card I must have:
• Linda Moorcombe
• 415-872-6041
• lindamoorcombe@quellmail.net
• This area will need to be updated once I complete my schooling.

```html
<!DOCTYPE html>
<html lang="en">
<head>
<meta charset="utf-8">
<title>Thriving Tables – Business Card</title>
<link href="https://fonts.googleapis.com/css2?family=Questrial&family=Gelasio:wght@700&display=swap" rel="stylesheet">
<style>
  :root {
    --brand-green: #95c12b;
    --name-green: #8dbf2e;
    --earth-brown: #9b8a80;
    --tagline-grey: #7a7a7a;
    --card-edge: #d9d9d9;
    --paper: #ffffff;
  }
  html, body {
    margin: 0;
    padding: 0;
    overflow: hidden;
    background: var(--paper);
  }
  .canvas {
    position: relative;
    width: 1200px;
    height: 358px;
    overflow: hidden;
    background: var(--paper);
  }
  .card {
    position: absolute;
    top: 0;
    width: 585px;
    height: 358px;
    box-sizing: border-box;
  }
  .card--front {
    left: 0;
    background: var(--paper);
    border: 2px solid var(--card-edge);
  }
  .card--back {
    left: 615px;
    background: var(--brand-green);
    border: 2px solid var(--card-edge);
  }
  .brand-ring {
    position: absolute;
    left: 232px;
    top: 87px;
  }
  .brand-name {
    position: absolute;
    left: 0;
    width: 100%;
    top: 210px;
    margin: 0;
    text-align: center;
    font-family: "Questrial", sans-serif;
    font-weight: 400;
    font-size: 33px;
    color: var(--name-green);
    letter-spacing: 0.5px;
  }
  .brand-tagline {
    position: absolute;
    left: 0;
    width: 100%;
    top: 252px;
    margin: 0;
    text-align: center;
    font-family: "Questrial", sans-serif;
    font-size: 19px;
    color: var(--tagline-grey);
    letter-spacing: 1.6px;
  }
  .back-ring {
    position: absolute;
    left: 75px;
    top: 128px;
  }
  .divider {
    position: absolute;
    left: 215px;
    top: 112px;
    width: 2px;
    height: 132px;
    background: var(--paper);
  }
  .contact {
    position: absolute;
    left: 242px;
    top: 138px;
    margin: 0;
    font-family: "Gelasio", serif;
    font-weight: 700;
    font-size: 18.5px;
    line-height: 27px;
    color: var(--paper);
    font-style: normal;
  }
  .contact span { display: block; }
</style>
</head>
<body>
<main class="canvas">
  <section class="card card--front" aria-label="Card front">
    <svg class="brand-ring" width="118" height="118" viewBox="0 0 118 118" aria-hidden="true">
      <circle cx="59" cy="59" r="55" fill="none" stroke="var(--earth-brown)" stroke-width="4.5"/>
    </svg>
    <h1 class="brand-name">Thriving Tables</h1>
    <p class="brand-tagline">healthy eating made easy</p>
  </section>

  <section class="card card--back" aria-label="Card back">
    <svg class="back-ring" width="118" height="118" viewBox="0 0 118 118" aria-hidden="true">
      <circle cx="59" cy="59" r="55" fill="none" stroke="var(--paper)" stroke-width="4.5"/>
    </svg>
    <div class="divider"></div>
    <address class="contact">
      <span class="contact-name">Linda Moorcombe</span>
      <span class="contact-phone">415-872-6041</span>
      <span class="contact-email">lindamoorcombe@quellmail.net</span>
    </address>
  </section>
</main>
</body>
</html>
```